Mr. Kelpie Restaurant Menu Design

I would like for you to please create a menu design for my seafood restaurant called Mr. Kelpie. I uploaded the logo of my restaurant and would like the same colors and font to be used on the menu. The headings of my menu should include the following:
What's your catch?
What's your sauce?
How "Hot" can you go?
Medium?
Mild?
Wild?
Soups
Paella
Katsu
Add Ons
Sweet Cravings
Thirsty?
It would be nice to see something creative and simple preferably one page.
I already uploaded my logo on the brief section.
Thank you.
Target Market(s)
Family friendly
Industry/Entity Type
Seafood Restaurant
Look and feel

```html
<!DOCTYPE html>
<html lang="en">
<head>
<meta charset="utf-8">
<title>Mr. Kelpie Restaurant Menu</title>
<link href="https://fonts.googleapis.com/css2?family=Fredoka:wght@600;700&family=Archivo:wght@700;800&family=Open+Sans:wght@400;600&display=swap" rel="stylesheet">
<style>
:root{
  --orange:#f07d22;
  --cream:#fde7cf;
  --blue:#29a3e0;
  --navy:#14314f;
  --ink:#111111;
  --white:#ffffff;
  --outline:#3a2418;
}
*{margin:0;padding:0;box-sizing:border-box}
html,body{width:848px;height:1200px;overflow:hidden;background:var(--white)}
.menu{position:relative;width:848px;height:1200px;overflow:hidden;font-family:"Archivo",Arial,sans-serif;color:var(--ink)}
.scene{position:absolute;inset:0;background:linear-gradient(180deg,#f4c99a 0%,#f7d8b0 20%,#f3b978 40%,#e9a06a 55%,#b88b7a 66%,#7e7e86 78%,#5d6f7a 88%,#8fa6ac 100%)}
.scene-chair{position:absolute;left:440px;top:640px;width:408px;height:470px;background:linear-gradient(180deg,rgba(240,200,120,.55) 0%,rgba(232,90,110,.55) 40%,rgba(90,190,200,.55) 80%,rgba(255,255,255,.3) 100%)}
.bands{position:absolute;inset:0}
.logo-art{position:absolute;left:336px;top:36px;width:176px;height:176px;border-radius:50%;background:var(--blue);border:6px solid var(--white)}
.brand{position:absolute;left:0;right:0;top:212px;text-align:center;font-family:"Fredoka",sans-serif;font-weight:700;font-size:56px;line-height:1;color:var(--white)}
.brand-sub{position:absolute;left:0;right:0;top:280px;text-align:center;font-family:"Fredoka",sans-serif;font-weight:700;font-size:24px;color:var(--blue);-webkit-text-stroke:1px var(--navy)}
.tagline{position:absolute;left:0;right:0;top:314px;text-align:center;font-family:"Fredoka",sans-serif;font-weight:700;font-size:21px;color:var(--white);-webkit-text-stroke:.8px var(--ink);word-spacing:3px}
.heat{position:absolute;left:0;right:0;top:340px;text-align:center;font-family:"Fredoka",sans-serif;font-weight:700;font-size:52px;color:var(--blue);-webkit-text-stroke:2px var(--navy);word-spacing:14px}
.section-title{position:absolute;font-family:"Fredoka",sans-serif;font-weight:700;font-size:30px;line-height:1.2;color:var(--white);-webkit-text-stroke:1.5px var(--outline);text-shadow:2px 2px 0 var(--orange),-2px -2px 0 var(--orange),2px -2px 0 var(--orange),-2px 2px 0 var(--orange)}
.item{position:absolute;width:290px}
.item-name{font-weight:800;font-size:16px;line-height:1.15}
.item-desc{font-weight:700;font-size:11px;line-height:1.35;margin-top:2px}
.col-left .item-desc{max-width:282px}
.col-right .item-desc{max-width:240px}
.col-right .drink .item-desc{max-width:205px}
.price{position:absolute;top:-3px;font-family:"Open Sans",sans-serif;font-weight:600;font-size:19px}
.col-left .price{left:246px}
.col-right .price{left:255px}
.contact{position:absolute;left:82px;font-family:"Open Sans",sans-serif;font-weight:600;font-size:17px;color:var(--white);display:flex;align-items:center;gap:14px}
.contact svg{width:26px;height:26px}
.find-us{position:absolute;left:384px;top:1156px;font-family:"Open Sans",sans-serif;font-weight:600;font-size:17px;color:var(--white)}
.social{position:absolute;top:1146px;width:38px;height:38px;border-radius:4px;background:var(--white);opacity:.9}
</style>
</head>
<body>
<main class="menu">
  <div class="scene" role="img" aria-label="Photograph of a sunset beach with a striped deck chair by the sea"></div>
  <div class="scene-chair" role="img" aria-label="Colourful striped beach chair"></div>

  <svg class="bands" width="848" height="1200" viewBox="0 0 848 1200" aria-hidden="true">
    <path d="M0 0H848V95C640 80 240 80 0 110Z" fill="var(--orange)"/>
    <path d="M0 110C240 80 640 80 848 95" fill="none" stroke="var(--white)" stroke-width="5" opacity=".85"/>
    <path d="M0 128C240 100 640 100 848 115" fill="none" stroke="var(--cream)" stroke-width="4" opacity=".8"/>
    <path d="M0 148C240 122 640 122 848 135" fill="none" stroke="var(--white)" stroke-width="3" opacity=".6"/>
    <rect x="0" y="272" width="848" height="134" fill="var(--orange)"/>
    <path d="M0 1040C240 1030 620 1030 848 1038V1200H0Z" fill="var(--orange)"/>
    <path d="M0 1048C240 1038 620 1040 848 1046" fill="none" stroke="var(--white)" stroke-width="5" opacity=".9"/>
    <path d="M0 1068C240 1058 620 1060 848 1066" fill="none" stroke="var(--cream)" stroke-width="4" opacity=".8"/>
    <path d="M0 1086C240 1076 620 1078 848 1084" fill="none" stroke="var(--white)" stroke-width="3" opacity=".7"/>
  </svg>

  <div class="logo-art" role="img" aria-label="Restaurant mascot emblem"></div>
  <div class="brand">Mr. Kelpie</div>
  <div class="brand-sub">Restaurant</div>
  <div class="tagline">WHAT’S YOUR CATCH? &nbsp;WHAT’S YOUR SAUCE? &nbsp;HOW “HOT” CAN YOU GO?</div>
  <div class="heat">Medium? Mild? Wild?</div>

  <section class="col-left">
    <h2 class="section-title" style="left:82px;top:432px">Soups</h2>
    <div class="item" style="left:81px;top:482px"><div class="item-name">Tuna Carpaccio</div><div class="item-desc">Poached lobster, honey tomato, avocado, tuna tapenade</div><span class="price">$30</span></div>
    <div class="item" style="left:81px;top:534px"><div class="item-name">Cheese soufflé</div><div class="item-desc">Morels crème, arugula salad and hazelnuts</div><span class="price">$30</span></div>
    <div class="item" style="left:81px;top:574px"><div class="item-name">Lobster salad</div><div class="item-desc">Herb and cauliflower salad, lemon cress, citrus dressing</div><span class="price">$30</span></div>
    <div class="item" style="left:81px;top:626px"><div class="item-name">Baked chermoula prawns</div><div class="item-desc">Stuffed with scallops, eggplant romesco, almond and pistachio</div><span class="price">$30</span></div>
    <div class="item" style="left:81px;top:678px"><div class="item-name">Prawn and calamari salad</div><div class="item-desc">Cured salmon, mango, crisp vegetables.</div><span class="price">$30</span></div>

    <h2 class="section-title" style="left:82px;top:718px">Paella</h2>
    <div class="item" style="left:81px;top:764px"><div class="item-name">King Crab Rillette</div><div class="item-desc">Watermelon, smoked trout, herb salad</div><span class="price">$20</span></div>
    <div class="item" style="left:81px;top:804px"><div class="item-name">Robian Salad</div><div class="item-desc">Arugula, halloumi and pomegranate</div><span class="price">$20</span></div>

    <h2 class="section-title" style="left:82px;top:846px">Katsu</h2>
    <div class="item" style="left:81px;top:892px"><div class="item-name">Salmon roulade</div><div class="item-desc">Basil tabouleh, marinated daikon, citra leaves</div><span class="price">$20</span></div>
    <div class="item" style="left:81px;top:932px"><div class="item-name">Pan fried Scallops</div><div class="item-desc">Stuffed calamari, squid ink risotto, micro herbs</div><span class="price">$20</span></div>
  </section>

  <section class="col-right">
    <h2 class="section-title" style="left:470px;top:436px">Add Ons</h2>
    <div class="item" style="left:440px;top:496px"><div class="item-name">Robian Salad</div><div class="item-desc">Arugula, halloumi and pomegranate</div><span class="price">$10.75</span></div>
    <div class="item" style="left:440px;top:548px"><div class="item-name">Salmon roulade</div><div class="item-desc">Basil tabouleh, marinated daikon, citra leaves</div><span class="price">$9.75</span></div>
    <div class="item" style="left:440px;top:599px"><div class="item-name">Pan fried Scallops</div><div class="item-desc">Stuffed calamari, squid ink risotto, micro herbs</div><span class="price">$8.25</span></div>

    <h2 class="section-title" style="left:466px;top:648px">Sweet Cravings</h2>
    <div class="item" style="left:440px;top:698px"><div class="item-name">Homemade Tiramisu</div><div class="item-desc">Layers of marscapone cheese and lady fingers soaked in coffee</div><span class="price" style="top:8px">$8.25</span></div>
    <div class="item" style="left:440px;top:765px"><div class="item-name">Jamaica Mud Cake</div><div class="item-desc">Dark chocolate sponge with a middle layer of chocolate ganache</div><span class="price" style="top:8px">$8.25</span></div>
    <div class="item" style="left:440px;top:832px"><div class="item-name">Bianco &amp; Nero</div><div class="item-desc">Profiterole filled with vanilla custard and coverture of milk chocolate</div><span class="price">$8.25</span></div>

    <h2 class="section-title" style="left:478px;top:889px">Thirsty?</h2>
    <div class="item drink" style="left:440px;top:950px"><div class="item-desc">Filter Coffe, decaf coffee, plain hot chocolate</div><span class="price" style="top:-4px">$8.25</span></div>
    <div class="item drink" style="left:440px;top:997px"><div class="item-desc">Assorted premium “Leaf Lark” teas</div><span class="price" style="top:-6px">$8.25</span></div>
    <div class="item drink" style="left:440px;top:1028px"><div class="item-desc">Hot chocolate with cream</div><span class="price" style="top:-6px">$8.25</span></div>
  </section>

  <div class="contact" style="top:1118px">
    <svg viewBox="0 0 26 26" aria-hidden="true"><circle cx="13" cy="13" r="13" fill="var(--blue)"/><path d="M6 13.5L13 7l7 6.5M8.5 12v7h3.5v-4h2v4h3.5v-7" fill="var(--white)" stroke="var(--white)" stroke-width="1.2" stroke-linejoin="round"/></svg>
    <span>Your Address</span>
  </div>
  <div class="contact" style="top:1153px">
    <svg viewBox="0 0 26 26" aria-hidden="true"><circle cx="13" cy="13" r="13" fill="var(--blue)"/><path d="M6 12c0-3 3-5 7-5s7 2 7 5l-2.5 1-1.5-2.5h-6L8.5 13Z M9 15h8l1 4H8Z" fill="var(--white)"/></svg>
    <span>0140-7781-306</span>
  </div>
  <div class="find-us">Find us @Mr.Kelpie on</div>
  <div class="social" style="left:578px"></div>
  <div class="social" style="left:629px"></div>
  <div class="social" style="left:680px"></div>
  <div class="social" style="left:728px"></div>
</main>
</body>
</html>
```